https://dorvakel.com

We need a cool technology design for our Managed IT Services company. We are located in Coral Springs Florida. We provide all IT services and support for small to medium sized businesses. We would like to see designs that use our blue and white colors from our website.

```html
<!DOCTYPE html>
<html lang="en">
<head>
<meta charset="utf-8">
<title>Dorvakel Business Card</title>
<link href="https://fonts.googleapis.com/css2?family=Lato:wght@400;700;900&display=swap" rel="stylesheet">
<style>
  :root {
    --navy: #102e52;
    --white: #ffffff;
    --backdrop: #e9e6e2;
    --text-dark: #1d2430;
    --shadow: rgba(0, 0, 0, 0.22);
  }
  * { box-sizing: border-box; margin: 0; padding: 0; }
  html, body {
    width: 1200px;
    height: 1200px;
    overflow: hidden;
    background: var(--backdrop);
    font-family: "Lato", sans-serif;
  }
  .canvas { position: relative; width: 1200px; height: 1200px; }
  .card {
    position: absolute;
    left: 223px;
    width: 754px;
    height: 430px;
    border-radius: 29px;
    box-shadow: 0 18px 30px var(--shadow);
  }
  .card-front { top: 145px; background: var(--navy); }
  .card-back { top: 638px; background: var(--white); }

  .front-wordmark {
    position: absolute;
    left: 0; right: 0;
    top: 158px;
    text-align: center;
    color: var(--white);
    font-weight: 700;
    font-size: 100px;
    line-height: 1;
    letter-spacing: -1px;
  }

  .back-wordmark {
    position: absolute;
    left: 119px;
    top: 84px;
    color: var(--navy);
    font-weight: 700;
    font-size: 79px;
    line-height: 1;
    letter-spacing: -1px;
  }
  .person-name {
    position: absolute;
    left: 121px;
    top: 196px;
    color: var(--navy);
    font-weight: 700;
    font-size: 27px;
    letter-spacing: 1px;
  }
  .person-title {
    position: absolute;
    left: 121px;
    top: 232px;
    color: var(--text-dark);
    font-size: 17px;
    letter-spacing: 0.5px;
  }
  .contact-list {
    position: absolute;
    left: 121px;
    top: 294px;
    list-style: none;
  }
  .contact-item {
    display: flex;
    align-items: center;
    height: 28px;
    color: var(--text-dark);
    font-size: 17px;
    letter-spacing: 0.5px;
  }
  .contact-icon {
    width: 16px;
    height: 16px;
    margin-right: 13px;
    fill: var(--navy);
  }
  .address {
    position: absolute;
    right: 68px;
    top: 322px;
    text-align: right;
    color: var(--text-dark);
    font-size: 17px;
    line-height: 28px;
    letter-spacing: 0.5px;
    padding-right: 13px;
    border-right: 3px solid var(--navy);
  }
</style>
</head>
<body>
<main class="canvas">
  <section class="card card-front">
    <div class="front-wordmark">DORVAKEL</div>
  </section>

  <section class="card card-back">
    <div class="back-wordmark">DORVAKEL</div>
    <div class="person-name">MARCUS ELLERY</div>
    <div class="person-title">Founder &amp; CEO</div>

    <ul class="contact-list">
      <li class="contact-item">
        <svg class="contact-icon" viewBox="0 0 24 24" aria-hidden="true"><path d="M6.6 10.8c1.4 2.8 3.8 5.1 6.6 6.6l2.2-2.2c.3-.3.7-.4 1-.2 1.1.4 2.3.6 3.6.6.6 0 1 .4 1 1V20c0 .6-.4 1-1 1C10.6 21 3 13.4 3 4c0-.6.4-1 1-1h3.5c.6 0 1 .4 1 1 0 1.3.2 2.5.6 3.6.1.3 0 .7-.2 1z"/></svg>
        (954) 555-0142
      </li>
      <li class="contact-item">
        <svg class="contact-icon" viewBox="0 0 24 24" aria-hidden="true"><path d="M2 11 22 3l-4 18-6-5-3 4v-6l10-9-12 8z"/></svg>
        m.ellery@dorvakel.com
      </li>
      <li class="contact-item">
        <svg class="contact-icon" viewBox="0 0 24 24" aria-hidden="true"><path d="M12 2a10 10 0 1 0 0 20 10 10 0 0 0 0-20zm-1 17.9A8 8 0 0 1 4.2 10L9 14.8v1c0 1.1.9 2 2 2zm6.9-2.5c-.3-.8-1-1.4-1.9-1.4h-1v-3c0-.6-.4-1-1-1H8v-2h2c.6 0 1-.4 1-1V7h2c1.1 0 2-.9 2-2v-.4a8 8 0 0 1 2.9 12.8z"/></svg>
        www.dorvakel.com
      </li>
    </ul>

    <address class="address" style="font-style: normal;">
      1875 W Palm Crest Blvd #120<br>
      Coral Springs, Florida 33065
    </address>
  </section>
</main>
</body>
</html>
```